Wordpress Design Project

We are a Computer / Information Technology Company that will focus on the after-hours technical support for Home and Businesses.

I'm looking to have the home page as a static page with a links to blog, about us.

www.rkwidget.com.au is my web site.

Please do not chage uploaded logo's, do not copy current logo on website use uploaded files only, thanks.
Updates

Project Deadline Extended
Reason: No idea how this was posted with only 2 days!!

Cheers

Marcus

Project Deadline Extended
Reason: I have asked for some changes from designers.

Target Market(s)

Home and Small office/home office, or SOHO Computer users.

Industry/Entity Type

Computer

Requirements
Should not have
• After hours tech support added to logo.

```html
<!DOCTYPE html>
<html lang="en">
<head>
<meta charset="utf-8">
<title>RK Widget – After Hours Tech Support</title>
<link href="https://fonts.googleapis.com/css2?family=Arimo:ital,wght@0,400;0,700;1,400&display=swap" rel="stylesheet">
<style>
  :root {
    --night: #000000;
    --steel: #9b9b9b;
    --steel-line: #5a5a5a;
    --ink: #2e2e2e;
    --paper: #ffffff;
    --blue-top: #2a8ad6;
    --blue-bottom: #0b5ea6;
    --blue-edge: #06467e;
    --dot-idle: #dcdcdc;
    --dot-live: #1d76c9;
    --hero-dark: #1c1c1c;
    --hero-mid: #4a4a4a;
    --hero-green: #5d9a2a;
  }
  * { box-sizing: border-box; margin: 0; padding: 0; }
  html, body { width: 1200px; height: 785px; overflow: hidden; }
  body {
    position: relative;
    font-family: "Arimo", Arial, sans-serif;
    background: var(--steel);
    color: var(--ink);
  }
  .top-band { position: absolute; left: 0; top: 0; width: 1200px; height: 291px; background: var(--night); }

  .brand { position: absolute; left: 142px; top: 30px; display: flex; align-items: center; gap: 10px; }
  .brand-mark { width: 40px; height: 40px; border-radius: 50%; background: #8c8c8c; }
  .brand-name { font-size: 28px; font-weight: 700; color: var(--blue-top); letter-spacing: 0.5px; }

  .social { position: absolute; left: 948px; top: 14px; display: flex; gap: 6px; }
  .social span { width: 22px; height: 22px; border-radius: 2px; display: block; }
  .social .s1 { background: #3b5998; }
  .social .s2 { background: #1a78b4; }
  .social .s3 { background: #2aa9e0; }
  .social .s4 { background: #e8337d; }

  .main-nav {
    position: absolute; left: 445px; top: 41px; width: 613px; height: 38px;
    background: linear-gradient(var(--blue-top), var(--blue-bottom));
    border: 1px solid var(--blue-edge); border-radius: 4px;
    display: flex;
  }
  .main-nav a {
    color: var(--paper); text-decoration: none; font-size: 15px;
    display: flex; align-items: center; justify-content: center;
    border-right: 1px solid var(--blue-edge);
  }
  .main-nav a:last-child { border-right: none; }

  .slider { position: absolute; left: 141px; top: 100px; width: 677px; height: 317px; background: var(--paper); border-radius: 3px; box-shadow: 0 16px 18px -10px rgba(0,0,0,.55); }
  .slide {
    position: absolute; left: 8px; top: 7px; width: 662px; height: 279px;
    background: radial-gradient(ellipse at 60% 40%, var(--hero-green) 0%, var(--hero-mid) 35%, var(--hero-dark) 80%);
  }
  .pager { position: absolute; left: 295px; top: 297px; display: flex; gap: 8px; }
  .pager span { width: 16px; height: 16px; border-radius: 50%; background: var(--dot-idle); border: 1px solid #c4c4c4; }
  .pager .is-active { background: var(--dot-live); border-color: var(--dot-live); }

  .services { position: absolute; left: 830px; top: 99px; width: 229px; height: 318px; background: var(--paper); box-shadow: 0 16px 18px -10px rgba(0,0,0,.55); }
  .services h2 {
    height: 37px; padding: 0 12px; line-height: 38px; font-size: 15px; font-weight: 400; color: var(--paper);
    background: linear-gradient(var(--blue-top), var(--blue-bottom)); border-radius: 3px 3px 0 0;
  }
  .services ul { list-style: none; margin: 13px 14px 0 15px; }
  .services li { font-size: 13px; color: #333; height: 25.3px; line-height: 22px; border-bottom: 1px dotted #9a9a9a; white-space: nowrap; letter-spacing: -0.1px; }

  .ticker { position: absolute; left: 141px; top: 443px; width: 918px; height: 41px; background: var(--paper); font-size: 12px; font-style: italic; color: #333; padding-left: 78px; line-height: 48px; white-space: nowrap; }

  .column { position: absolute; top: 508px; }
  .column h2 { font-size: 19px; font-weight: 400; color: var(--paper); padding: 0 0 3px 2px; border-bottom: 4px solid var(--steel-line); }
  .column p { font-size: 13px; line-height: 25.3px; color: #2f2f2f; }
  .welcome { left: 141px; width: 290px; }
  .welcome h2 { width: 274px; }
  .welcome p { margin-top: 10px; padding-left: 4px; }
  .schedule { left: 458px; width: 275px; }
  .schedule .lead { color: var(--paper); margin-top: 10px; }
  .hours { margin-top: 25px; width: 310px; display: grid; grid-template-columns: 160px auto; font-size: 13px; line-height: 25.3px; white-space: nowrap; }
  .contact { left: 785px; width: 274px; }
  .contact p { padding-left: 6px; }
  .contact .address { margin-top: 10px; }
  .contact .phone { margin-top: 25px; }
  .contact .mail { color: var(--paper); }
  .divider { position: absolute; top: 537px; width: 2px; height: 169px; background: linear-gradient(#eee, #cfcfcf); }

  .site-footer { position: absolute; left: 0; top: 727px; width: 1200px; height: 58px; background: var(--night); color: var(--paper); font-size: 12px; }
  .footer-links { position: absolute; left: 0; width: 1200px; top: 12px; text-align: center; padding-left: 97px; }
  .footer-links a { color: var(--paper); text-decoration: none; }
  .copyright { position: absolute; left: 146px; top: 39px; font-style: italic; }
  .credit { position: absolute; right: 146px; top: 39px; font-style: italic; }
</style>
</head>
<body>
  <div class="top-band"></div>

  <header>
    <div class="brand"><span class="brand-mark"></span><span class="brand-name">RK Widget</span></div>
    <div class="social" aria-label="Social links"><span class="s1"></span><span class="s2"></span><span class="s3"></span><span class="s4"></span></div>
    <nav class="main-nav">
      <a href="#" style="width:96px">Home</a>
      <a href="#" style="width:123px">About Us</a>
      <a href="#" style="width:121px">Services</a>
      <a href="#" style="width:124px">News</a>
      <a href="#" style="flex:1">Quick Contact</a>
    </nav>
  </header>

  <section class="slider">
    <div class="slide" role="img" aria-label="Photo of a green desktop computer tower beside a flat screen monitor"></div>
    <div class="pager"><span></span><span></span><span></span><span class="is-active"></span></div>
  </section>

  <aside class="services">
    <h2>Services</h2>
    <ul>
      <li>No job is too small Apex or PC:</li>
      <li>Home ADSL.</li>
      <li>Wireless.</li>
      <li>Virus removal.</li>
      <li>Vantage configuration</li>
      <li style="border-bottom:none">and installation.</li>
      <li>Apex configuration and installation.</li>
      <li>Hardware.</li>
    </ul>
  </aside>

  <div class="ticker">Latest news goes here, latest news goes here, latest news goes here, latest news goes here latest news goes here, latest news goes here...</div>

  <section class="column welcome">
    <h2>Welcome</h2>
    <p>Welcome to company, company detail goes<br>here, welcome to company, company detail<br>goes here, welcome to company, company<br>detail goes here, welcome to company,<br>company detail goes here, welcome to company,<br>company detail goes here,</p>
  </section>

  <div class="divider" style="left:432px"></div>

  <section class="column schedule">
    <h2>Schedule</h2>
    <p class="lead">After Hours Appointments Available</p>
    <div class="hours">
      <span>Mon: 6:00 PM-9:00 PM</span><span>Tue: 6:00 PM-9:00 PM</span>
      <span>Wed: 6:00 PM-9:00 PM</span><span>Thu: 6:00 PM-9:00 PM</span>
      <span>Fri: 6:00 PM-9:00 PM</span><span>Sat: 10:00 AM-9:00 PM</span>
      <span>Sun: 10:00 AM-9:00 PM</span>
    </div>
  </section>

  <div class="divider" style="left:768px"></div>

  <section class="column contact">
    <h2>Contact</h2>
    <p class="address">Address goes here, address goes here,<br>address goes here, address goes here,</p>
    <p class="phone">Phone: xxxx xx xx xx</p>
    <p>Email: <span class="mail">info@rkwidget.com.au</span></p>
  </section>

  <footer class="site-footer">
    <div class="footer-links"><a href="#">Home</a> | <a href="#">About Us</a> | <a href="#">Services</a> | <a href="#">Contact Us</a> | <a href="#">Privacy Policy</a> | <a href="#">Term &amp; Conditions</a></div>
    <div class="copyright">Copyright 2011 @rkwidget.com.au &nbsp;| &nbsp;All rights are reserved</div>
    <div class="credit">Design &amp; developed by................</div>
  </footer>
</body>
</html>
```